Business software developers new website

We need to redesign our website. Our current website is http://www.quorvanta.net/index.html, which is outdated and needs a new look. We moved out from web design and have concentrated more on the back end of the systems, for example, system support and security and cloud-based applications. Our major clients include both private and government sectors. We would like to see some designs that are all in one page, simple and clean. Prefer illustrator or obstructed images instead of real-life photos. Must look futuristic yet friendly. Attached the new logo for your references and good luck.

Target Market(s)

Medium to big company for their IT or data management. Either improve or upgrade their current system.

Industry/Entity Type

Business Software

Number of Pages Required

1 page

Colors

Designer to choose colors to be used in the design.

Requirements
Must have
• Simple and clean. Individual assets must be provided in the correct size and format(png or jpeg). Prefer Goggle fonts. Even though the logo color is red, grey and black, still prefer some modern colors that go well with red. When design, must consider the possibility to convert it into responsive.
Nice to have
• White background
Should not have
• real life photos, no slider

```html
<!DOCTYPE html>
<html lang="en">
<head>
<meta charset="utf-8">
<title>quorvanta.net</title>
<link href="https://fonts.googleapis.com/css2?family=Raleway:wght@300;400;500;600;700;800&family=Roboto+Condensed:wght@400&display=swap" rel="stylesheet">
<style>
:root{
  --red:#e52d3b;
  --red-deep:#d41f3a;
  --red-glow:rgba(229,45,59,.18);
  --ink:#1d1f24;
  --text:#333;
  --white:#fff;
  --line:#d4d6dc;
  --field:#b7b9c0;
}
*{box-sizing:border-box;margin:0;padding:0}
html,body{width:1200px;height:2249px;overflow:hidden;background:var(--white)}
body{position:relative;font-family:'Raleway',sans-serif;color:var(--text)}
.abs{position:absolute}

/* header */
.site-header{left:60px;top:0;width:1080px;height:138px;background:var(--white);box-shadow:0 10px 26px var(--red-glow);border-radius:0 0 10px 10px}
.brand{left:88px;top:38px;font-family:'Roboto Condensed',sans-serif;font-size:56px;color:var(--ink);letter-spacing:.5px}
.nav{display:flex;gap:15px;left:624px;top:51px}
.nav a{display:block;height:38px;line-height:36px;padding:0 14px;border:1.5px solid var(--red);border-radius:20px;color:var(--red);font-size:16px;text-decoration:none}
.nav a.active{background:linear-gradient(120deg,var(--red),var(--red-deep));color:var(--white);box-shadow:0 4px 12px var(--red-glow)}

/* feature cards */
.card{width:291px;height:387px;top:238px;background:var(--white);box-shadow:0 10px 24px rgba(20,24,40,.09);border-radius:6px;overflow:hidden}
.card-top{position:absolute;left:0;top:0;width:100%;height:137px;background:linear-gradient(135deg,var(--red) 0%,var(--red-deep) 100%)}
.card-frame{position:absolute;left:6px;top:8px;right:6px;bottom:8px;border:1px solid var(--red);border-radius:3px}
.card-art{position:absolute;left:50%;top:18px;width:116px;height:116px;margin-left:-58px;border-radius:50%;background:radial-gradient(circle,rgba(255,255,255,.16),rgba(255,255,255,.04))}
.card h2{position:absolute;left:0;right:0;top:54px;text-align:center;color:var(--white);font-size:29px;font-weight:700}
.card p{position:absolute;left:20px;right:20px;top:159px;text-align:center;font-size:15px;line-height:17.8px;letter-spacing:.6px;color:#444}
.card .news-title{top:210px;font-size:19px;letter-spacing:1px}
.card .news-body{top:250px}

/* section headings */
.tag{height:55px;background:linear-gradient(120deg,var(--red),var(--red-deep));color:var(--white);font-size:29px;font-weight:700;text-align:center;line-height:55px;border-radius:4px 4px 0 0}

.company{left:103px;top:711px;width:685px;height:475px;border:1px solid var(--red);border-radius:8px;box-shadow:0 10px 30px rgba(20,24,40,.05)}
.company-text{left:121px;top:798px;width:650px;font-size:17.5px;line-height:21.2px;color:#222}
.company-text p{margin-bottom:21px}

.contact-card{left:838px;top:933px;width:288px;height:138px;background:var(--white);border-top:1px solid #999;box-shadow:0 10px 24px rgba(20,24,40,.1);border-radius:0 0 8px 8px}
.contact-card h3{position:absolute;left:16px;top:12px;font-size:27px;font-weight:500;color:#111}
.contact-card .row{position:absolute;left:66px;font-size:14.5px;color:#111}
.contact-card b{font-weight:700;margin-right:6px}
.icon-tab{top:898px;width:50px;height:35px;border-radius:7px 7px 0 0;border:1.5px solid var(--red)}

.divider{left:103px;top:1259px;width:1037px;height:1px;background:var(--line)}

.faq-q{left:148px;font-size:15.5px;color:#222}
.faq-line{left:109px;width:683px;height:1px;background:var(--red)}
.faq-answer{left:110px;top:1471px;width:685px;height:119px;border:1px solid var(--red);border-radius:8px}
.faq-answer p{position:absolute;left:8px;top:26px;right:20px;font-size:13.5px;line-height:16.8px;color:#222}
.faq-answer .cap{font-size:26px;font-weight:300;color:var(--red);line-height:14px}

.affil{left:833px;top:1390px;width:283px;height:200px;background:var(--white);box-shadow:0 8px 20px rgba(20,24,40,.08);border-radius:0 0 6px 6px}
.affil-frame{position:absolute;left:11px;top:8px;right:9px;bottom:7px;border:1px solid var(--red)}
.affil-name{position:absolute;left:0;right:0;top:82px;text-align:center;font-size:24px;font-weight:700;color:#111}

/* footer */
.footer{left:46px;top:1744px;width:1143px;height:505px;background:linear-gradient(160deg,var(--red) 0%,var(--red-deep) 100%)}
.outline-tag{height:55px;border:2px solid var(--white);color:var(--white);font-size:29px;font-weight:700;text-align:center;line-height:51px;width:282px;top:1780px;border-radius:3px}
.philo{left:94px;top:1858px;width:380px;color:var(--white);font-weight:700;font-size:17.5px;line-height:29.5px}
.field{background:var(--white);border-radius:26px;color:var(--field);font-size:15px;font-weight:300;padding-left:57px}
.send{left:538px;top:2158px;width:185px;height:50px;background:var(--white);border-radius:26px;color:var(--red);font-size:16px;font-weight:700;text-align:center;line-height:50px;box-shadow:0 6px 16px rgba(0,0,0,.12)}
</style>
</head>
<body>

<header class="abs site-header"></header>
<div class="abs brand">quorvanta.net</div>
<nav class="abs nav">
  <a class="active" href="#">HOME</a>
  <a href="#">OUR SERVICES</a>
  <a href="#">OUR CLIENT</a>
  <a href="#">CONTACT</a>
</nav>

<section class="abs card" style="left:101px">
  <div class="card-top"><div class="card-art" role="img" aria-label="Faint illustration of server documents"></div></div>
  <div class="card-frame"></div>
  <h2>ABOUT US</h2>
  <p>We build and support the back end of business systems for private and government clients. Our work covers system support, security hardening, cloud-based applications and data management. We are known for reliable delivery, clear rates and an individual approach to each client, upgrading the systems you already run at very competitive prices!</p>
</section>

<section class="abs card" style="left:454px">
  <div class="card-top"><div class="card-art" role="img" aria-label="Faint illustration of a cloud network"></div></div>
  <div class="card-frame"></div>
  <h2>OUR CLIENT</h2>
  <p>We work with medium to large companies and government agencies. We are highly experienced in the long term support of comprehensive business systems, providing first class cloud migration, security audits, maintenance, data management and system upgrades.</p>
</section>

<section class="abs card" style="left:808px">
  <div class="card-top"><div class="card-art" style="width:106px;height:106px;margin-left:-53px;top:22px" role="img" aria-label="Faint illustration of a megaphone"></div></div>
  <div class="card-frame"></div>
  <h2>NEWS</h2>
  <p class="news-title">Cloud:</p>
  <p class="news-body">Quorvanta.net launches managed cloud services.</p>
</section>

<section class="abs company"></section>
<div class="abs tag" style="left:109px;top:717px;width:283px">OUR COMPANY</div>
<div class="abs company-text">
  <p>Quorvanta.net is an Australian based business software company that builds, secures and supports the systems behind your organisation, for clients worldwide.</p>
  <p>Our work is based on system support, security and cloud-based applications.</p>
  <p>Being oriented towards innovative productivity in our work, we come up with essential tools for data management and system upgrades. Our engineers focus on delivering secure back-end solutions for medium and large organizations and government agencies. The team of purposeful and experienced professionals works hard to extract maximum performance from modern cloud technologies.</p>
  <p>Providing the best quality of service and excellence of support we established a global presence in the software market. Our clients come from all over the world.</p>
  <p>Click here for more information on the services we provide.</p>
</div>

<div class="abs tag" style="left:835px;top:795px;width:283px">QUICK CONTACT</div>
<div class="abs icon-tab" style="left:932px;background:var(--red)">
  <svg width="50" height="35" viewBox="0 0 50 35"><path d="M19 9c2-1 3 0 4 3l-2 2c1 3 3 5 5 6l2-2c3 1 4 2 3 4-2 3-5 2-8 0-3-3-6-7-6-10 0-1 1-2 2-3z" fill="none" stroke="#fff" stroke-width="1.6"/></svg>
</div>
<div class="abs icon-tab" style="left:985px;background:var(--white)">
  <svg width="50" height="35" viewBox="0 0 50 35"><rect x="13" y="11" width="22" height="15" fill="#e52d3b"/><path d="M13 11l11 9 11-9M13 26l8-7M35 26l-8-7" fill="none" stroke="#fff" stroke-width="1.3"/></svg>
</div>
<div class="abs contact-card">
  <h3>Call us today</h3>
  <div class="row" style="top:63px"><b>phone</b>+61 700 481 226</div>
  <div class="row" style="top:98px"><b>Mobile</b>+61 040 318 775 2</div>
</div>

<div class="abs divider"></div>

<div class="abs tag" style="left:109px;top:1328px;width:283px">FAQ</div>
<svg class="abs" style="left:114px;top:1410px" width="22" height="22" viewBox="0 0 22 22"><path d="M3 5l8 7 8-7M3 11l8 7 8-7" fill="none" stroke="#e52d3b" stroke-width="1.5"/></svg>
<div class="abs faq-q" style="top:1410px">How much does a system upgrade by Quorvanta.net cost?</div>
<div class="abs faq-line" style="top:1450px"></div>
<div class="abs faq-answer">
  <p><span class="cap">T</span>here are quite a few factors that are going to affect the ultimate cost of your system upgrade. These factors include how many users and servers you run, whether you will move data to the cloud, the security work involved, and how much ongoing support your team will need</p>
</div>
<svg class="abs" style="left:149px;top:1457px" width="30" height="15" viewBox="0 0 30 15"><path d="M0 15L15 1 30 15" fill="#fff" stroke="#e52d3b" stroke-width="1"/></svg>
<svg class="abs" style="left:114px;top:1623px" width="22" height="22" viewBox="0 0 22 22"><path d="M4 3l7 8-7 8M10 3l7 8-7 8" fill="none" stroke="#e52d3b" stroke-width="1.5"/></svg>
<div class="abs faq-q" style="top:1623px">How secure is cloud hosting by Quorvanta.net?</div>
<div class="abs faq-line" style="top:1663px"></div>

<div class="abs tag" style="left:833px;top:1328px;width:283px">AFFILIATES</div>
<div class="abs affil">
  <div class="affil-frame"></div>
  <div class="affil-name">Kestrel Studio</div>
</div>

<footer class="abs footer"></footer>
<div class="abs outline-tag" style="left:103px">PHILOSOPHI</div>
<div class="abs outline-tag" style="left:538px">PHILOSOPHI</div>
<p class="abs philo">&nbsp;As system developers, we understand that a secure and reliable back end is a vital component of modern day business for companies of today. This is why our support and security team work with all of our clients to ensure their systems and cloud applications deliver to their users.</p>
<div class="abs field" style="left:538px;top:1870px;width:275px;height:50px;line-height:50px">What is your name ?</div>
<div class="abs field" style="left:838px;top:1870px;width:276px;height:50px;line-height:50px">Where i can reply ?</div>
<div class="abs field" style="left:538px;top:1932px;width:577px;height:189px;padding-top:22px">Talk to me</div>
<div class="abs send">SEND MESSAGE</div>

</body>
</html>
```